Calendar Design Project: 2025 with Specific Edits

This is a straightforward project where your creativity can shine!
Simply take the existing 2024 calendar and adapt it for 2025 by incorporating the new photos I've attached.
Please keep the overall concept of the 2024 calendar intact—your focus will be on enhancing it with fresh visuals.

I can't wait to see your amazing designs!
I am looking for a talented graphic designer to create a new 2025 calendar with specific adjustments.
Pictures attached.
Requirements:
Calendar Size: 52cm x 34cm
March Folder:
Adjust the image named "attached - DJI-0025" to make the circular road darker to match the rest of the design.
May Folder:
Modify the circled area in the May image to ensure it looks consistent with the other road (reference file: "attached - After").
November Folder:
Clear out the circled area in the November image (reference file: "attached - After1").
Please let me know if you have any questions or need further clarification.
I added to my breif a design i made last year for same client.
2025, calendar should be vertical and not horizontal. and some of the photos attache are "Before" and "After" please include together inside each month of the calendar.
Thank you!
Feel free to adjust any details as necessary!

Hello talented designers!

I’m excited to share that this is my 14th project on the ArtHarbor platform, and I’ve been fortunate to have successful collaborations in the past. I'm looking forward to creating a new 2025 calendar with your help, and I believe that with your creativity and skills, we can make this project a success as well!

I hope to establish a long-term relationship with a talented team like yours. As an added incentive, I will be offering a bonus for the winner, and I may select more than one winner, so everyone has a chance to shine!

Let’s make something amazing together!

Best
Update:
cancel or before, only place the After picture

Requirements
Must have
• Project Overview Objective: Create a 2025 calendar using the provided images, maintaining the design concept from the 2024 calendar but enhancing it with new visuals. Format: Vertical layout (52cm x 34cm).

```html
<!DOCTYPE html>
<html lang="en">
<head>
<meta charset="utf-8">
<title>KORVA Calendar 2025 – January</title>
<link rel="stylesheet" href="https://fonts.googleapis.com/css2?family=Roboto:wght@400;500;700&family=Saira+Condensed:wght@400&display=swap">
<style>
  :root {
    --green: #27b36b;
    --green-dark: #1d7a3a;
    --leaf: #8cc63f;
    --leaf-pale: #eaf5d8;
    --weekend: #c9e6c0;
    --weekday: #ececec;
    --ink: #231f20;
    --grey: #555555;
    --white: #ffffff;
  }
  * { box-sizing: border-box; margin: 0; padding: 0; }
  html, body { width: 785px; height: 1200px; overflow: hidden; background: var(--white); }
  body { font-family: "Roboto", Arial, sans-serif; color: var(--ink); }
  .page { position: relative; width: 785px; height: 1200px; overflow: hidden; }

  .hero { position: absolute; left: 0; top: 0; width: 785px; height: 640px; }

  .brand { position: absolute; left: 56px; top: 62px; display: flex; align-items: center; gap: 10px; }
  .brand-mark { width: 34px; height: 34px; background: var(--green); }
  .brand-name { font-size: 64px; font-weight: 700; color: var(--ink); letter-spacing: 2px; line-height: 1; }
  .brand-line { position: absolute; left: 56px; top: 131px; font-size: 10.5px; font-weight: 400; color: var(--ink); letter-spacing: -0.2px; }

  .title-calendar { position: absolute; left: 41px; top: 588px; font-size: 31px; font-weight: 400; color: var(--green); letter-spacing: -0.5px; }
  .title-year { position: absolute; left: 43px; top: 617px; font-size: 70px; font-weight: 700; color: var(--ink); letter-spacing: -2px; line-height: 1; }
  .title-month { position: absolute; left: 298px; top: 641px; font-size: 45px; font-weight: 400; color: var(--grey); letter-spacing: -1.5px; line-height: 1; }

  .month-grid { position: absolute; left: 37px; top: 706px; display: grid;
    grid-template-columns: repeat(7, 66px); column-gap: 4.8px;
    grid-template-rows: 38px repeat(5, 49px); row-gap: 10.5px; }
  .month-grid .day-head { display: flex; align-items: center; justify-content: center; font-size: 9px; font-weight: 500; color: var(--ink); background: var(--weekday); }
  .month-grid .cell { background: var(--weekday); display: flex; align-items: flex-end; padding: 0 0 4px 5px; font-size: 22px; font-weight: 700; color: var(--ink); line-height: 1; }
  .month-grid .weekend { background: var(--weekend); color: var(--green-dark); }
  .month-grid .day-head.weekend { color: var(--green-dark); }
  .month-grid .first-row { margin-top: -1px; }

  .mini { position: absolute; left: 567px; width: 186px; }
  .mini-dec { top: 702px; }
  .mini-feb { top: 891px; }
  .mini-title { font-size: 13.5px; font-weight: 500; color: var(--ink); letter-spacing: -0.4px; display: flex; align-items: center; gap: 6px; height: 20px; }
  .mini-title .mini-year { color: var(--green); font-weight: 400; border-left: 1.5px solid #b5b5b5; padding-left: 6px; }
  .mini-grid { margin-top: 5px; display: grid; grid-template-columns: repeat(7, 25px); column-gap: 1.5px;
    grid-template-rows: 13px repeat(6, 18px); row-gap: 4px; }
  .mini-grid .mh { font-size: 3.6px; font-weight: 500; display: flex; align-items: center; justify-content: center; background: var(--weekday); color: var(--ink); }
  .mini-grid .mh.weekend { background: var(--weekend); color: var(--green-dark); }
  .mini-grid .mh { margin-bottom: 4px; }
  .mini-grid .mc { background: var(--weekday); font-size: 8px; font-weight: 500; display: flex; align-items: flex-end; padding: 0 0 2px 3px; color: var(--ink); }
  .mini-grid .mc.weekend { background: var(--weekend); color: var(--green-dark); }

  .footer { position: absolute; left: 38px; top: 1050px; width: 712px; height: 36px; display: flex; align-items: center; }
  .footer-brand { display: flex; align-items: center; gap: 4px; width: 80px; }
  .footer-brand .brand-mark { width: 10px; height: 10px; }
  .footer-brand .brand-name { font-size: 18px; letter-spacing: 0.5px; }
  .contact { display: flex; gap: 14px; margin-left: 36px; font-family: "Saira Condensed", "Arial Narrow", sans-serif; font-size: 11.5px; color: var(--ink); white-space: nowrap; }
  .contact .label { color: var(--green); }
</style>
</head>
<body>
<main class="page">

  <svg class="hero" viewBox="0 0 785 640" xmlns="http://www.w3.org/2000/svg">
    <defs>
      <linearGradient id="leafTop" x1="0" y1="0" x2="1" y2="0">
        <stop offset="0" stop-color="#f3f9ea"/>
        <stop offset="0.55" stop-color="#a9d75e"/>
        <stop offset="1" stop-color="#86c33c"/>
      </linearGradient>
      <linearGradient id="leafBottom" x1="0" y1="0" x2="1" y2="0">
        <stop offset="0" stop-color="#dcefc4"/>
        <stop offset="0.6" stop-color="#9bd050"/>
        <stop offset="1" stop-color="#7fbf33"/>
      </linearGradient>
      <linearGradient id="swoosh" x1="0" y1="0" x2="1" y2="0">
        <stop offset="0" stop-color="#ffffff" stop-opacity="1"/>
        <stop offset="0.7" stop-color="#ffffff" stop-opacity="0.75"/>
        <stop offset="1" stop-color="#ffffff" stop-opacity="0.1"/>
      </linearGradient>
      <linearGradient id="siteTones" x1="0" y1="0" x2="1" y2="1">
        <stop offset="0" stop-color="#a99c8e"/>
        <stop offset="0.35" stop-color="#9fb0b8"/>
        <stop offset="0.6" stop-color="#c98f64"/>
        <stop offset="1" stop-color="#7f9fb8"/>
      </linearGradient>
    </defs>
    <rect x="0" y="0" width="785" height="640" fill="#ffffff"/>
    <rect x="0" y="0" width="785" height="210" fill="url(#leafTop)"/>
    <path d="M0 60 C160 140 420 120 785 30 L785 90 C460 110 220 140 0 178 Z" fill="url(#swoosh)"/>
    <path d="M0 0 L785 0 L785 12 C520 40 250 20 0 32 Z" fill="#ffffff" opacity="0.85"/>
    <path role="img" aria-label="Aerial photograph of a bridge construction site with precast beams through a town"
          d="M0 172 C220 145 470 108 785 88 L785 455 C700 470 650 520 520 525 C360 515 200 525 0 542 Z"
          fill="url(#siteTones)"/>
    <path d="M0 542 C200 510 360 505 520 518 C640 526 700 470 785 450 L785 580 C700 630 560 640 380 612 C220 590 100 565 0 560 Z" fill="url(#leafBottom)"/>
    <path d="M0 560 C100 565 220 590 380 612 C560 640 700 630 785 580 L785 640 L0 640 Z" fill="#ffffff"/>
  </svg>

  <div class="brand"><span class="brand-mark"></span><span class="brand-name">KORVA</span></div>
  <div class="brand-line">BUILDING BETTER COMMUNITIES</div>

  <div class="title-calendar">CALENDAR</div>
  <div class="title-year">2025</div>
  <div class="title-month">JANUARY</div>

  <section class="month-grid" aria-label="January 2025">
    <div class="day-head weekend">SUNDAY</div><div class="day-head">MONDAY</div><div class="day-head">TUESDAY</div><div class="day-head">WEDNESDAY</div><div class="day-head">THURSDAY</div><div class="day-head">FRIDAY</div><div class="day-head weekend">SATURDAY</div>
    <div class="cell weekend"></div><div class="cell"></div><div class="cell"></div><div class="cell">1</div><div class="cell">2</div><div class="cell">3</div><div class="cell weekend">4</div>
    <div class="cell weekend">5</div><div class="cell">6</div><div class="cell">7</div><div class="cell">8</div><div class="cell">9</div><div class="cell">10</div><div class="cell weekend">11</div>
    <div class="cell weekend">12</div><div class="cell">13</div><div class="cell">14</div><div class="cell">15</div><div class="cell">16</div><div class="cell">17</div><div class="cell weekend">18</div>
    <div class="cell weekend">19</div><div class="cell">20</div><div class="cell">21</div><div class="cell">22</div><div class="cell">23</div><div class="cell">24</div><div class="cell weekend">25</div>
    <div class="cell weekend">26</div><div class="cell">27</div><div class="cell">28</div><div class="cell">29</div><div class="cell">30</div><div class="cell">31</div><div class="cell weekend"></div>
  </section>

  <section class="mini mini-dec" aria-label="December 2024">
    <div class="mini-title">DECEMBER <span class="mini-year">2024</span></div>
    <div class="mini-grid">
      <div class="mh weekend">SUNDAY</div><div class="mh">MONDAY</div><div class="mh">TUESDAY</div><div class="mh">WEDNESDAY</div><div class="mh">THURSDAY</div><div class="mh">FRIDAY</div><div class="mh weekend">SATURDAY</div>
      <div class="mc weekend">1</div><div class="mc">2</div><div class="mc">3</div><div class="mc">4</div><div class="mc">5</div><div class="mc">6</div><div class="mc weekend">7</div>
      <div class="mc weekend">8</div><div class="mc">9</div><div class="mc">10</div><div class="mc">11</div><div class="mc">12</div><div class="mc">13</div><div class="mc weekend">14</div>
      <div class="mc weekend">15</div><div class="mc">16</div><div class="mc">17</div><div class="mc">18</div><div class="mc">19</div><div class="mc">20</div><div class="mc weekend">21</div>
      <div class="mc weekend">22</div><div class="mc">23</div><div class="mc">24</div><div class="mc">25</div><div class="mc">26</div><div class="mc">27</div><div class="mc weekend">28</div>
      <div class="mc weekend">29</div><div class="mc">30</div><div class="mc">31</div><div class="mc"></div><div class="mc"></div><div class="mc"></div><div class="mc weekend"></div>
    </div>
  </section>

  <section class="mini mini-feb" aria-label="February 2025">
    <div class="mini-title">FEBRUARY <span class="mini-year">2025</span></div>
    <div class="mini-grid">
      <div class="mh weekend">SUNDAY</div><div class="mh">MONDAY</div><div class="mh">TUESDAY</div><div class="mh">WEDNESDAY</div><div class="mh">THURSDAY</div><div class="mh">FRIDAY</div><div class="mh weekend">SATURDAY</div>
      <div class="mc weekend"></div><div class="mc"></div><div class="mc"></div><div class="mc"></div><div class="mc"></div><div class="mc"></div><div class="mc weekend">1</div>
      <div class="mc weekend">2</div><div class="mc">3</div><div class="mc">4</div><div class="mc">5</div><div class="mc">6</div><div class="mc">7</div><div class="mc weekend">8</div>
      <div class="mc weekend">9</div><div class="mc">10</div><div class="mc">11</div><div class="mc">12</div><div class="mc">13</div><div class="mc">14</div><div class="mc weekend">15</div>
      <div class="mc weekend">16</div><div class="mc">17</div><div class="mc">18</div><div class="mc">19</div><div class="mc">20</div><div class="mc">21</div><div class="mc weekend">22</div>
      <div class="mc weekend">23</div><div class="mc">24</div><div class="mc">25</div><div class="mc">26</div><div class="mc">27</div><div class="mc">28</div><div class="mc weekend"></div>
    </div>
  </section>

  <footer class="footer">
    <div class="footer-brand"><span class="brand-mark"></span><span class="brand-name">KORVA</span></div>
    <div class="contact">
      <span><span class="label">T</span>: +2340005550123</span>
      <span><span class="label">E</span>: hello@korvabuild.com</span>
      <span><span class="label">W</span>: www.korvabuild.com</span>
      <span><span class="label">A</span>: 27 Palmgrove Lane, Off Harbour Crescent, Eastfield, Lakeview City</span>
    </div>
  </footer>

</main>
</body>
</html>
```